QUORVIX - Sydney Based Technology Consultancy -Logo & Business Card design

Who are we?
-
Quorvix is an emerging and advanced technology consulting and professional services business based in Sydney, Australia. Quorvix specialising in increasing value to organisations through the effective use of current and emerging technologies, ensuring that technology is a sustainable catalyst to attaining stated business goals.

We pride ourselves in challenging the norm.

What do we want?
-
We are looking to update our "Brand" we already have a simple “home grown” logo and we are now looking for a new one, once we have this updated logo and businesses look and feel though the business card design we will refresh our website with the new logo and design thus updating the Companies overall look at feel.

Our current site is www.quorvix-example.net.au is a very basic wordpress site and we will be updating it once we have the new logo and designs done

Our initial thoughts on the new Quorvix identity are
• Logo Concept
- One of the key things is obviously the 8
- I was thinking that a logo that had 8 as the core of the logo would be cool,
- Almost like having a “ring” or hoop that is twisted to form an 8 with different services scribed on the inside.
- So we would have a Large 8 and the inside would have ring each service or section engraved.

• Brand / web Feel
- Simple
- Professional
- Innovative
- Clear
- Destination
- Unique
- Impartial
- Safe
- Leading edge
- Familiar

- Emerging technologies
- White and ice / glacier blue
- The familiar feel of the Brindle web site
- Embedded specialist Video clips

• Portfolio of Services
- Quorvix – A smart place for Smart people
- Quorvix – we provide the process to take ideas from awareness to reality
- Focus should be on the brand quality consistent clear local knowledge with regional, national, theatre and global presence

Access to Specialists
- Emerging technologies
- Sustainability
- Collaboration
- Data centre
- Virtualisation

• Adjacent ideas under the one Brand
- Tembrosk – Enable Business Collaboration
- Plinsk – Infrastructure Virtualisation
- morvo - smart people and processes
- skandel - Emerging technologies
- brunhavel - business to technology integration
- tolpin - Smart Infrastructure
- yusk – Connected communities
- dwol - sustainability

Target Market(s)

Australia, New Zealand and Asia pacific organisations that are typically English speaking.
Markets
- IT & Technology partners
- Banking and Finance
- Health

Industry/Entity Type

Business

Requirements
Must have
• Logo
Business cards
Colour pallette
3D Logo
Nice to have
• Style guide
Designer who can also assist with new Wordpress design
Should not have
• we don't want cheap looking, overtly flashy or gimmicky logo.

```html
<!DOCTYPE html>
<html lang="en">
<head>
<meta charset="utf-8">
<title>Quorvix Business Card</title>
<link rel="stylesheet" href="https://fonts.googleapis.com/css2?family=Bodoni+Moda:wght@400;500&display=swap">
<style>
  :root {
    --page-bg: #ffffff;
    --card-edge: #9a9b9c;
    --card-light: #e3e4e5;
    --card-mid: #d2d4d5;
    --card-dark: #c6c8c9;
    --ink: #6b6c6d;
    --ink-soft: #7c7d7e;
    --dot: #ffffff;
  }
  * { margin: 0; padding: 0; box-sizing: border-box; }
  html, body {
    width: 1200px;
    height: 821px;
    overflow: hidden;
    background: var(--page-bg);
  }
  .canvas {
    position: relative;
    width: 1200px;
    height: 821px;
    font-family: "Bodoni Moda", "Didot", serif;
  }
  .card {
    position: absolute;
    border: 3px solid var(--card-edge);
    overflow: hidden;
  }
  .card-surface {
    position: absolute;
    inset: 0;
    background:
      linear-gradient(90deg, var(--card-mid) 0%, var(--card-light) 18%, var(--card-mid) 34%, var(--card-light) 52%, var(--card-dark) 68%, var(--card-light) 84%, var(--card-mid) 100%);
  }
  .card-front {
    left: 0;
    top: 0;
    width: 648px;
    height: 471px;
  }
  .card-back {
    left: 552px;
    top: 346px;
    width: 641px;
    height: 471px;
  }
  .brand-name {
    position: absolute;
    left: 0;
    right: 0;
    top: 168px;
    text-align: center;
    font-size: 112px;
    font-weight: 400;
    line-height: 1;
    letter-spacing: 2px;
    color: var(--ink);
  }
  .contact-block {
    position: absolute;
    left: 0;
    right: 0;
    top: 268px;
    text-align: center;
    color: var(--ink);
  }
  .person-name {
    font-size: 46px;
    font-weight: 400;
    line-height: 1.1;
  }
  .person-role {
    font-size: 38px;
    font-weight: 400;
    line-height: 1.1;
  }
  .contact-line {
    margin-top: 22px;
    font-size: 19px;
    color: var(--ink-soft);
    line-height: 1.5;
    white-space: nowrap;
  }
  .sep {
    display: inline-block;
    width: 6px;
    height: 6px;
    border-radius: 50%;
    background: var(--dot);
    vertical-align: middle;
    margin: 0 6px;
  }
</style>
</head>
<body>
<main class="canvas">
  <section class="card card-front">
    <div class="card-surface" role="img" aria-label="Brushed pale grey woodgrain texture"></div>
    <div class="brand-name">QUORVIX</div>
  </section>

  <section class="card card-back">
    <div class="card-surface" role="img" aria-label="Brushed pale grey woodgrain texture"></div>
    <div class="contact-block">
      <h1 class="person-name">Daniel Hartley</h1>
      <p class="person-role">Managing Director</p>
      <p class="contact-line">
        P: 123 4567<span class="sep"></span>F: 123 4567<span class="sep"></span>E: daniel.hartley@quorvix-example.net.au
      </p>
      <p class="contact-line contact-web">
        <span class="sep"></span>www.quorvix-example.net.au<span class="sep"></span>
      </p>
    </div>
  </section>
</main>
</body>
</html>
```